Hydraulics Company Business Card Design

Modern business card design for a hydraulics company.
Our company colours are - black, orange and white.
I would like the following contact details included-
Name
Position
Phone number
Email
Website
Street Address

I have attached our company logo.
I would like the back of the card white.

Thank you.

```html
<!DOCTYPE html>
<html lang="en">
<head>
<meta charset="utf-8">
<title>Corbett Hydraulics – Business Card</title>
<link rel="stylesheet" href="https://fonts.googleapis.com/css2?family=Montserrat:wght@400;500;600;700;800&display=swap">
<style>
  :root {
    --orange: #f7981c;
    --black: #1e1e1e;
    --white: #ffffff;
    --ink: #2b2b2b;
    --backdrop: #2a2a2a;
  }
  * { margin: 0; padding: 0; box-sizing: border-box; }
  html, body { width: 1200px; height: 875px; overflow: hidden; }
  body {
    background: var(--backdrop);
    font-family: "Montserrat", sans-serif;
    position: relative;
  }
  .card {
    position: absolute;
    top: 289px;
    width: 520px;
    height: 297px;
    border-radius: 18px;
    overflow: hidden;
    box-shadow: 0 18px 40px rgba(0,0,0,.45);
  }
  .card--front { left: 50px; background: var(--black); }
  .card--back { left: 630px; background: var(--white); }

  .wordmark {
    color: var(--orange);
    font-weight: 800;
    line-height: 1;
    white-space: nowrap;
  }
  .card--front .wordmark {
    position: absolute;
    left: 0; right: 0; top: 50%;
    transform: translateY(-50%);
    text-align: center;
    font-size: 46px;
  }

  .band { position: absolute; left: 0; top: 0; width: 520px; height: 170px; }
  .card--back .wordmark {
    position: absolute;
    left: 128px; top: 80px;
    font-size: 36px;
  }

  .person { position: absolute; left: 42px; top: 178px; }
  .person__name { color: var(--orange); font-weight: 600; font-size: 21px; letter-spacing: .5px; }
  .person__role { color: var(--ink); font-size: 12px; margin-top: 2px; }

  .rule {
    position: absolute;
    left: 42px; right: 42px; top: 230px;
    height: 1px;
    background: var(--orange);
  }

  .contacts { position: absolute; left: 42px; top: 240px; list-style: none; }
  .contacts li {
    display: flex; align-items: center; gap: 8px;
    font-size: 11px; color: var(--ink); line-height: 16px;
  }
  .contacts svg { width: 10px; height: 10px; fill: var(--orange); }

  .address {
    position: absolute;
    right: 42px; top: 240px;
    text-align: right;
    font-size: 11px; line-height: 16px; color: var(--ink);
    font-style: normal;
  }
  .address__company { color: var(--orange); font-weight: 600; }
</style>
</head>
<body>

<section class="card card--front">
  <p class="wordmark">Corbett Hydraulics</p>
</section>

<section class="card card--back">
  <svg class="band" viewBox="0 0 520 170" aria-hidden="true">
    <path d="M0 0 H520 V150 H210 Q196 150 190 140 Q184 130 170 130 H0 Z" fill="var(--black)"/>
    <path d="M0 130 H170 Q184 130 190 140 Q196 150 210 150 H520" fill="none" stroke="var(--orange)" stroke-width="6"/>
  </svg>
  <p class="wordmark">Corbett Hydraulics</p>

  <div class="person">
    <p class="person__name">DANIEL REEVES</p>
    <p class="person__role">Founder &amp; CEO</p>
  </div>

  <div class="rule"></div>

  <ul class="contacts">
    <li>
      <svg viewBox="0 0 10 10"><path d="M2 0.5 L4 2.8 L3 4 Q4 6 6 7 L7.2 6 L9.5 8 L8 9.5 Q3.5 9.5 0.5 2 Z"/></svg>
      (123) 456-7890
    </li>
    <li>
      <svg viewBox="0 0 10 10"><path d="M0 2 H10 V8 H0 Z M0 2 L5 5.5 L10 2" /></svg>
      info@yourwebsitehere.com
    </li>
    <li>
      <svg viewBox="0 0 10 10"><circle cx="5" cy="5" r="5"/></svg>
      yourwebsitehere.com
    </li>
  </ul>

  <address class="address">
    <span class="address__company">Corbett Hydraulics</span><br>
    Street Address Here, City<br>
    State, Country, ZIP 123
  </address>
</section>

</body>
</html>
```